Lone Elm Cattle Website

I need a website for my cattle company. I will be sharing pictures of my herd along with selling my calves individually. I need the following pages:
About
Cattle Sales
Bulls
Cows/Heifers
Gallery
Contact Us

I just uploaded a few pictures, but I have a lot more!

```html
<!DOCTYPE html>
<html lang="en">
<head>
<meta charset="UTF-8">
<title>Lone Elm Cattle</title>
<link href="https://fonts.googleapis.com/css2?family=Poppins:wght@400;500;600&family=Trirong:wght@500;600&display=swap" rel="stylesheet">
<style>
:root{
  --brown:#5b4330;
  --brown-dark:#3e2d20;
  --ink:#1d1d1d;
  --text:#3b3b3b;
  --hero-bg:#ebe9e9;
  --cream:#fcf8f3;
  --night:#17120d;
  --gold:#c9a878;
  --star:#f26a1b;
  --white:#ffffff;
}
*{margin:0;padding:0;box-sizing:border-box}
html,body{width:1200px;height:4060px;overflow:hidden}
body{font-family:'Poppins',sans-serif;color:var(--text);background:var(--white);position:relative}
.abs{position:absolute}
.btn{position:absolute;display:flex;align-items:center;justify-content:center;background:var(--brown);color:var(--white);border-radius:40px;font-size:16px;text-decoration:none}
.photo{position:absolute}
.ornament{position:absolute;height:8px}
.ornament::before{content:"";position:absolute;left:0;right:0;top:3px;height:2px;background:var(--brown)}
.ornament::after{content:"";position:absolute;left:50%;top:0;width:8px;height:8px;margin-left:-4px;border-radius:50%;background:var(--brown)}
.ornament i{position:absolute;top:1px;width:6px;height:6px;border-radius:50%;background:var(--brown)}
.ornament i:first-child{left:-3px}.ornament i:last-child{right:-3px}
.ornament.gold::before,.ornament.gold::after,.ornament.gold i{background:var(--gold)}
.section-title{position:absolute;left:0;width:1200px;text-align:center;font-family:'Trirong',serif;font-weight:600;font-size:56px;line-height:62px;color:var(--brown);letter-spacing:1px}

/* header */
.site-header{position:absolute;top:0;left:0;width:1200px;height:133px;background:var(--white)}
.brand{position:absolute;left:70px;top:48px;display:flex;align-items:center;gap:10px;font-family:'Trirong',serif;font-weight:600;font-size:24px;line-height:32px;color:var(--brown)}
.brand-dot{width:22px;height:22px;border-radius:50%;background:var(--brown)}
.nav a{position:absolute;top:53px;font-size:17px;line-height:24px;color:#333;text-decoration:none}
.nav a.active{color:var(--brown)}
.nav a.active::after{content:"";position:absolute;left:0;right:0;bottom:-6px;height:2px;background:var(--brown)}

/* hero */
.hero{position:absolute;top:133px;left:0;width:1200px;height:522px;background:var(--hero-bg)}
.hero-photo{left:0;top:0;width:580px;height:522px;background:linear-gradient(90deg,#4d3a25 0%,#5c4a2c 35%,#6b7040 70%,rgba(235,233,233,0) 100%)}
.hero-welcome{left:603px;top:60px;font-size:31px;line-height:40px;color:var(--ink)}
.hero-title{left:600px;top:108px;font-family:'Trirong',serif;font-weight:600;font-size:88px;line-height:98px;color:var(--ink);letter-spacing:1px;white-space:nowrap}
.hero-text{left:603px;top:328px;width:520px;font-size:12.5px;line-height:21px;color:#333}

/* about */
.about-title{left:133px;top:748px;font-family:'Trirong',serif;font-weight:600;font-size:56px;line-height:62px;color:var(--brown)}
.about-text{left:133px;top:853px;width:510px;font-size:14px;line-height:23.3px;color:#333}
.about-photo{left:692px;top:695px;width:369px;height:453px;border-radius:0 130px 0 130px;background:linear-gradient(160deg,#8a8a72 0%,#6e6a4c 40%,#5b4328 70%,#6d7a42 100%)}

/* sales */
.sales{position:absolute;top:1195px;left:0;width:1200px;height:753px;background:var(--cream)}
.card{position:absolute;top:213px;width:324px;height:462px;background:var(--white);box-shadow:0 2px 10px rgba(0,0,0,.1);text-align:center}
.card .photo{left:0;top:0;width:324px;height:279px}
.card h3{position:absolute;top:305px;width:100%;font-size:22px;line-height:30px;font-weight:600;color:var(--ink)}
.card p{position:absolute;top:344px;width:100%;font-size:17px;line-height:24px;color:#222}
.card .btn{left:81px;top:377px;width:162px;height:51px;font-size:18px}

/* gallery */
.gallery-photo{border-radius:6px}

/* reviews */
.reviews{position:absolute;top:3032px;left:0;width:1200px;height:538px;background:linear-gradient(180deg,#1f1812 0%,#15100c 60%,#0f0b08 100%)}
.reviews .section-title{color:var(--gold)}
.avatar{left:550px;top:183px;width:94px;height:94px;border-radius:50%;border:3px solid #ddd;background:linear-gradient(160deg,#e6e0d6,#b9ab95)}
.review-text{left:290px;top:318px;width:620px;text-align:center;color:var(--white);font-size:14px;line-height:22px}
.reviewer{left:0;width:1200px;top:408px;text-align:center;color:var(--white);font-size:15px;line-height:22px;font-weight:500}
.stars{left:0;width:1200px;top:432px;text-align:center;color:var(--star);font-size:22px;line-height:26px;letter-spacing:3px}

/* footer */
.footer-brand{left:110px;top:3745px;width:280px;text-align:center;font-family:'Trirong',serif;font-weight:600;font-size:28px;line-height:36px;color:var(--brown)}
.social{top:3862px;width:36px;height:36px;border-radius:50%;background:var(--brown)}
.foot-head{top:3665px;font-family:'Trirong',serif;font-weight:600;font-size:23px;line-height:30px;color:var(--brown)}
.foot-rule{top:3703px;width:52px;height:2px;background:var(--brown)}
.links{left:508px;top:3736px;list-style:none}
.links li{position:relative;padding-left:22px;font-size:16px;line-height:22px;color:#333;height:32.5px}
.links li::before{content:"";position:absolute;left:0;top:8px;width:7px;height:7px;border-radius:50%;background:var(--brown-dark)}
.contact-item{left:813px;display:flex;align-items:flex-start;gap:14px;font-size:18px;color:#222;line-height:22px}
.contact-icon{width:37px;height:37px;border-radius:50%;background:var(--brown);flex:none;display:flex;align-items:center;justify-content:center}
.footer-line{left:68px;top:3985px;width:1065px;height:2px;background:#c9a878}
.copyright{left:0;width:1200px;top:4016px;text-align:center;font-size:13px;line-height:18px;color:#444}
</style>
</head>
<body>

<header class="site-header">
  <div class="brand"><span class="brand-dot"></span>Lone Elm Cattle</div>
  <nav class="nav">
    <a class="active" style="left:432px">Home</a>
    <a style="left:505px">About</a>
    <a style="left:577px">Cattle Sales</a>
    <a style="left:695px">Bulls</a>
    <a style="left:752px">Cows/Heifers</a>
    <a style="left:881px">Gallery</a>
  </nav>
  <a class="btn" style="left:959px;top:43px;width:173px;height:47px;font-size:17px">Contact Us</a>
</header>

<section class="hero">
  <div class="photo hero-photo" role="img" aria-label="Highland cattle grazing in a grassy meadow"></div>
  <p class="abs hero-welcome">welcome To</p>
  <h1 class="abs hero-title">LONE ELM<br>CATTLE</h1>
  <p class="abs hero-text">Lorem ipsum dolor sit amet, consectetur adipiscing elit, sed do eiusmod tempor incididunt ut labore et dolore magna aliqua. Quis ipsum suspendisse</p>
  <a class="btn" style="left:601px;top:383px;width:161px;height:56px">Know More</a>
</section>

<section>
  <h2 class="abs about-title">ABOUT US</h2>
  <div class="ornament" style="left:133px;top:822px;width:130px"><i></i><i></i></div>
  <p class="abs about-text">Lorem ipsum dolor sit amet, consectetur adipiscing elit, sed do eiusmod tempor incididunt ut labore et dolore magna aliqua. Ut enim ad minim veniam, quis nostrud exercitation ullamco laboris nisi ut aliquip ex ea commodo consequat. Duis aute irure dolor in reprehenderit in voluptate velit esse cillum dolore eu fugiat nulla pariatur. Excepteur sint occaecat cupidatat non proident, sunt in culpa qui officia deserunt mollit anim id est laborum.</p>
  <a class="btn" style="left:133px;top:1032px;width:148px;height:48px;font-size:14px">Read More</a>
  <div class="photo about-photo" role="img" aria-label="Highland cow standing in tall grass under trees"></div>
</section>

<section class="sales">
  <h2 class="section-title" style="top:82px">CATTLE SALES</h2>
  <div class="ornament" style="left:532px;top:155px;width:136px"><i></i><i></i></div>
  <article class="card" style="left:96px">
    <div class="photo" role="img" aria-label="Two bulls grazing side by side" style="background:linear-gradient(135deg,#2e2a26,#6b5c44 55%,#5d6b3a)"></div>
    <h3>BULLS</h3><p>$ 44.99 USD</p><a class="btn">View More</a>
  </article>
  <article class="card" style="left:440px">
    <div class="photo" role="img" aria-label="Pale shaggy cow grazing" style="background:linear-gradient(135deg,#3a3630,#d9cfb2 50%,#6d6a45)"></div>
    <h3>COWS</h3><p>$ 44.99 USD</p><a class="btn">View More</a>
  </article>
  <article class="card" style="left:784px">
    <div class="photo" role="img" aria-label="Dark heifer standing in a wet pasture" style="background:linear-gradient(135deg,#8fa26a,#2d2522 50%,#7c9358)"></div>
    <h3>HEIFERS</h3><p>$ 44.99 USD</p><a class="btn">View More</a>
  </article>
</section>

<section>
  <h2 class="section-title" style="top:2030px">GALLERY</h2>
  <div class="ornament" style="left:532px;top:2101px;width:136px"><i></i><i></i></div>
  <div class="photo gallery-photo" role="img" aria-label="Highland bull with long horns under a cloudy sky" style="left:79px;top:2157px;width:321px;height:302px;background:linear-gradient(180deg,#9db0c4,#6b4a30 55%,#a8926c)"></div>
  <div class="photo gallery-photo" role="img" aria-label="Black highland cow in snow" style="left:436px;top:2157px;width:328px;height:361px;background:linear-gradient(180deg,#eef2f4,#2a2a2c 55%,#e6ecef)"></div>
  <div class="photo gallery-photo" role="img" aria-label="Two highland cattle in a field" style="left:794px;top:2157px;width:321px;height:302px;background:linear-gradient(135deg,#6f99c8,#c9c0ad 40%,#7a4a26 75%)"></div>
  <div class="photo gallery-photo" role="img" aria-label="Golden highland calf on grass" style="left:84px;top:2505px;width:316px;height:362px;background:linear-gradient(160deg,#4e6a2e,#9a6a34 50%,#3f5a28)"></div>
  <div class="photo gallery-photo" role="img" aria-label="Fluffy highland calf lying in green grass" style="left:436px;top:2566px;width:325px;height:301px;background:linear-gradient(180deg,#6f9a3a,#b58a5a 50%,#4f8a2a)"></div>
  <div class="photo gallery-photo" role="img" aria-label="Highland cow in an open pasture" style="left:794px;top:2505px;width:321px;height:362px;background:linear-gradient(180deg,#d7dcdc,#8c5a36 55%,#4e7a3a)"></div>
  <svg class="abs" style="left:544px;top:2910px" width="70" height="32" viewBox="0 0 70 32" aria-hidden="true">
    <circle cx="15" cy="15" r="14" fill="#8f8378"/><path d="M18 9l-6 6 6 6" stroke="#fff" stroke-width="2.5" fill="none"/>
    <circle cx="52" cy="15" r="14" fill="#3e2d20"/><path d="M49 9l6 6-6 6" stroke="#fff" stroke-width="2.5" fill="none"/>
  </svg>
</section>

<section class="reviews">
  <h2 class="section-title" style="top:72px">CUSTOMER REVIEWS</h2>
  <div class="ornament gold" style="left:532px;top:144px;width:136px"><i></i><i></i></div>
  <div class="abs avatar" role="img" aria-label="Customer portrait"></div>
  <svg class="abs" style="left:215px;top:318px" width="26" height="34" viewBox="0 0 26 34" aria-hidden="true"><path d="M20 4L7 17l13 13" stroke="#c9a878" stroke-width="4" fill="none"/></svg>
  <svg class="abs" style="left:938px;top:318px" width="26" height="34" viewBox="0 0 26 34" aria-hidden="true"><path d="M6 4l13 13L6 30" stroke="#ffffff" stroke-width="4" fill="none"/></svg>
  <p class="abs review-text">Lorem ipsum dolor sit amet, consectetur adipiscing elit, sed do eiusmod tempor incididunt ut labore et dolore magna aliqua. Quis ipsum suspendisse ultrices gravida. Risus commodo viverra maecenas accumsan lacus vel facilisis.</p>
  <p class="abs reviewer">MARCUS REED</p>
  <p class="abs stars">★★★★★</p>
</section>

<footer>
  <p class="abs footer-brand">Lone Elm Cattle</p>
  <span class="abs social" style="left:182px"></span>
  <span class="abs social" style="left:232px"></span>
  <span class="abs social" style="left:278px"></span>

  <h4 class="abs foot-head" style="left:504px">LINKS</h4>
  <span class="abs foot-rule" style="left:504px"></span>
  <ul class="abs links">
    <li>About</li><li>Cattle Sales</li><li>Bulls</li><li>Cows/Heifers</li><li>Gallery</li><li>Contact Us</li>
  </ul>

  <h4 class="abs foot-head" style="left:813px">CONTACT US</h4>
  <span class="abs foot-rule" style="left:813px;width:95px"></span>
  <div class="abs contact-item" style="top:3735px">
    <span class="contact-icon"><svg width="18" height="20" viewBox="0 0 18 20"><path d="M9 1a6.5 6.5 0 0 0-6.5 6.5C2.5 12 9 19 9 19s6.5-7 6.5-11.5A6.5 6.5 0 0 0 9 1z" fill="#fff"/><circle cx="9" cy="7.5" r="2.5" fill="#5b4330"/></svg></span>
    <span>223,Lorem ipsum<br>Lorem ipsum,Lorem ipsum.</span>
  </div>
  <div class="abs contact-item" style="top:3803px;align-items:center">
    <span class="contact-icon"><svg width="18" height="18" viewBox="0 0 24 24"><path d="M6.6 10.8a15 15 0 0 0 6.6 6.6l2.2-2.2a1 1 0 0 1 1-.25 11.4 11.4 0 0 0 3.6.57 1 1 0 0 1 1 1V20a1 1 0 0 1-1 1A17 17 0 0 1 3 4a1 1 0 0 1 1-1h3.5a1 1 0 0 1 1 1c0 1.25.2 2.45.57 3.57a1 1 0 0 1-.25 1z" fill="#fff"/></svg></span>
    <span>8888 888 888</span>
  </div>
  <div class="abs contact-item" style="top:3855px;align-items:center">
    <span class="contact-icon"><svg width="18" height="14" viewBox="0 0 18 14"><rect x="1" y="1" width="16" height="12" rx="1.5" fill="none" stroke="#fff" stroke-width="1.6"/><path d="M1.5 2l7.5 6 7.5-6" fill="none" stroke="#fff" stroke-width="1.6"/></svg></span>
    <span>info@companyname.com</span>
  </div>

  <span class="abs footer-line"></span>
  <p class="abs copyright">© 2025 Company Name, Inc. All Rights Reserved.</p>
</footer>

</body>
</html>
```